Health & Fitness Author & Public Speaker Needs Visually Stunning Web Redesign!

It's time for a redesign of the home page for Beatrix Holloway's "Bright Fork Kitchen" website (www.brightforkkitchen.example). We have a VERY clear idea of what we want, so it really won't take a talented designer long to bring it to life.
The website itself is used to promote & sell her range of health & nutrition programs to a female audience, primarily aged 24 - 35 working in professional or semi professional occupations.
For a VERY comprehensive outline of exactly what we are after, please see the following attached files:
(1) 'Website - WireFrame' (layout, content/copy, visual design style we want along with the desired color scheme)
(2) 'Website - Style Guide' (these are the colours, and overall feel we want)
PLEASE REVIEW THIS IN FULL - THEY WILL GIVE YOU A VERY CLEAR IDEA OF WHAT WE WANT.
Most of the files you need are attached, but for more photos that you can use (of Beatrix, her programs, and food/meals) can be found at these URL's:
BEATRIX (profile photos):
https://www.filevault.example/s/k3m9p2x7q1/AbCdEf1234
ECOVERS
- Bright Fork Kitchen Guide (ebook): https://www.filevault.example/s/r8t4w6y2n5/GhIjKl5678
- 6 Week Total Momentum Course (ecourse): https://www.filevault.example/s/u1v5z9c3b7/MnOpQr9012
- E-Magazine Issues:
https://www.filevault.example/s/d2f6h8j4l0/StUvWx3456
STOCK IMAGES:
https://www.filevault.example/s/g7k1m5n9p3/YzAbCd7890
As we will need to revamp our existing Facebook page & other printed material, there may be the potential for further work for the successful designer in the future.
Thanks & Good Luck!
Desmond Farrow
Marketing & Business Development Manager
Bright Fork Kitchen

```html
<!DOCTYPE html>
<html lang="en">
<head>
<meta charset="utf-8">
<title>Bright Fork Kitchen</title>
<link rel="stylesheet" href="https://fonts.googleapis.com/css2?family=Lato:ital,wght@0,400;0,700;0,900;1,700&family=Questrial&family=Gochi+Hand&display=swap">
<style>
  :root {
    --ink: #1d1d1d;
    --pink: #ec1757;
    --navy: #0f1d44;
    --plum: #8c1f8f;
    --plum-soft: #b56cb8;
    --footer: #262626;
    --white: #ffffff;
    --field-border: #d9d9d9;
    --placeholder: #9a9a9a;
    --social: #4c5f86;
  }
  * { margin: 0; padding: 0; box-sizing: border-box; }
  html, body { width: 1200px; height: 1183px; overflow: hidden; background: var(--white); }
  body { position: relative; font-family: "Lato", Arial, sans-serif; color: var(--ink); font-size: 15px; line-height: 22px; }

  .content { position: absolute; left: 28px; top: 0; width: 832px; }
  .ticks { list-style: none; position: absolute; left: 0; width: 832px; }
  .ticks li { position: relative; padding-left: 19px; }
  .ticks li::before {
    content: ""; position: absolute; left: 5px; top: 7px;
    border-left: 6px solid var(--ink); border-top: 4.5px solid transparent; border-bottom: 4.5px solid transparent;
  }
  .goals { top: 15px; }
  .goals li { height: 29px; }
  .flaws { top: 327px; }
  .flaws li { line-height: 18px; margin-bottom: 11px; }
  .flaws li::before { top: 5px; }
  .copy { position: absolute; left: 0; width: 832px; }
  .copy-intro { top: 254px; }
  .copy-empathy { top: 568px; }
  .copy-credentials { top: 684px; }
  .copy-next { top: 775px; }

  .signup {
    position: absolute; left: 19px; top: 898px; width: 700px; height: 170px;
    background: var(--pink); color: var(--white); padding: 12px 14px;
  }
  .signup-title { font-weight: 700; font-size: 23px; line-height: 28px; letter-spacing: 0.2px; }
  .signup-sub { font-size: 15px; line-height: 20px; }
  .signup-form { position: absolute; left: 18px; top: 88px; display: flex; gap: 11px; }
  .field {
    width: 239px; height: 41px; background: var(--white); border: 1px solid var(--field-border);
    color: var(--placeholder); font-size: 15px; line-height: 39px; padding-left: 13px;
  }
  .signup-button {
    width: 166px; height: 41px; background: #111; border: 2px solid #555; color: var(--white);
    font-weight: 900; font-size: 22px; line-height: 37px; text-align: center; letter-spacing: 0.3px;
  }

  .kickstart-note {
    position: absolute; left: 740px; top: 828px; font-family: "Gochi Hand", cursive;
    color: var(--plum); font-size: 32px; line-height: 40px; white-space: nowrap;
  }
  .kickstart-pointer {
    position: absolute; left: 1121px; top: 860px; width: 36px; height: 52px; z-index: 2;
    background: linear-gradient(180deg, var(--plum-soft) 0%, var(--plum) 100%);
  }
  .kickstart {
    position: absolute; left: 733px; top: 898px; width: 443px; height: 170px;
    background: var(--navy); color: var(--white); padding: 17px 14px;
  }
  .kickstart-title { font-weight: 700; font-size: 21px; line-height: 23px; text-transform: uppercase; width: 300px; }
  .kickstart-text { font-size: 15px; line-height: 17px; margin-top: 16px; width: 270px; }
  .kickstart-cover {
    position: absolute; left: 333px; top: 22px; width: 96px; height: 140px;
    background: linear-gradient(160deg, #f4f1ec 0%, #e7d9cf 55%, #c86a4a 100%);
    box-shadow: 3px 3px 6px rgba(0,0,0,0.4);
  }

  .site-footer {
    position: absolute; left: 0; top: 1090px; width: 1200px; height: 93px;
    background: var(--footer); color: var(--white); font-family: "Questrial", Arial, sans-serif;
  }
  .footer-links { position: absolute; left: 33px; top: 30px; font-size: 18px; }
  .footer-links span.sep { margin: 0 14px; }
  .footer-copy { position: absolute; left: 33px; top: 63px; font-size: 13px; }
  .footer-contact { position: absolute; left: 793px; top: 37px; font-size: 18px; }
  .footer-contact strong { font-weight: 400; font-size: 22px; letter-spacing: 0.3px; }
  .footer-social { position: absolute; left: 1015px; top: 34px; display: flex; gap: 11px; }
  .footer-social span { width: 28px; height: 28px; background: var(--social); display: block; }
</style>
</head>
<body>
  <main class="content">
    <ul class="ticks goals">
      <li>To Lose weight (most ladies I work with want to lose between 5kg-10kg... sometimes more)</li>
      <li>Have more energy</li>
      <li>Stop feeling bloated and exhausted</li>
      <li>Stop feeling frustrated for eating the "wrong" things and not exercising "enough"</li>
      <li>Feel hot in your clothes, at work and when you go out</li>
      <li>Feel proud of yourself</li>
      <li>Still have a social life... with you know, friends and stuff!</li>
    </ul>

    <p class="copy copy-intro">Ok... sounds good so far right, but you're probably wondering what is about my method that's so different for all the others out there? Honestly, the problem with most other diet programs is that they:</p>

    <ul class="ticks flaws">
      <li>Ignore the importance of pleasure in your life for weight loss. (I think it's key)</li>
      <li>Aren't sustainable– (try and stop me from never eating a French pastry again &amp; see what happens)</li>
      <li>Don't teach you how to never need to be on another program, plan or diet again.</li>
      <li>Focus on what you need to cut out (I focus on what you need more of in your life to make it more pleasurable so you can<br>stop feeding the voids in your life with toxic food, booze, etc)</li>
      <li>Assume you want the same things as everyone else. They assume your definition of healthy should be the same as<br>everyone else's. (I'll teach you what works for you)</li>
      <li>Ignore the impact that stress has on your ability to shift weight (biochemistry can be cruel).</li>
    </ul>

    <p class="copy copy-empathy">I get it. I know and understand first hand your frustrations (I used to be you). <strong><em>I know you want it to be effortless. I know you want to not worry about putting on weight EVER, you want to just "Be"</em></strong>. You may have some pieces of the puzzle already, but they just never seem to gel together for long enough to get the outcome you truly crave - A hot body you're proud of with a healthy lifestyle you love. I get it. I understand. And I can help you get there.</p>

    <p class="copy copy-credentials">As a qualified Food &amp; Wellness Coach (and Personal Trainer), I've helped thousands of women (starting with myself) just like you over the last 7+ years to not just lose weight (that's nice) but take back control, regain self confidence and find peace with their bodies (that's better – trust me). You can do it to.</p>

    <p class="copy copy-next">So what now? First things first, sign up for my E-Magazine below (it's FREE!) to receive some really fantastic recipes, inspirational articles, workouts &amp; expert wellness tips each month.</p>
  </main>

  <section class="signup">
    <h2 class="signup-title">Get Slim, Boost Energy, And &nbsp;Create a Healthy Life You Love!</h2>
    <p class="signup-sub">Subscribe to my FREE monthly e-magazine &nbsp;for heaps of awesome recipes, workouts &amp; advice!</p>
    <div class="signup-form">
      <div class="field">Your first name</div>
      <div class="field">Your email id</div>
      <div class="signup-button">SIGN ME UP!</div>
    </div>
  </section>

  <p class="kickstart-note">Need a hand getting started</p>
  <div class="kickstart-pointer" role="img" aria-label="Hand-drawn curved arrow pointing down to the course box"></div>

  <section class="kickstart">
    <h2 class="kickstart-title">6 Week Total Momentum Course</h2>
    <p class="kickstart-text">Finally an easy to follow program to help you get slim &amp; eat well, but also help you create a Healthy Life you love!</p>
    <div class="kickstart-cover" role="img" aria-label="Course cover showing a plate of fresh healthy food"></div>
  </section>

  <footer class="site-footer">
    <nav class="footer-links">Privacy Policy<span class="sep">|</span>Returns &amp; Refunds<span class="sep">|</span>Contact</nav>
    <p class="footer-copy">© 2014 brightforkkitchen</p>
    <p class="footer-contact">Contact with <strong>BEATRIX</strong></p>
    <div class="footer-social" aria-label="Social links">
      <span></span><span></span><span></span><span></span>
    </div>
  </footer>
</body>
</html>
```